Party Favors and Decorations Business Needs A Business Card Design

We are in need of a Logo design and business card design for a new small business called Lark Meadow Designs. We create party decorations and favours for Bridal Showers, Baby Showers, Weddings Birthdays etc. This is a very personalized service based on Clients theme, colour, and style. We are looking for a high end elegant look. I have attached a file to the style I like including the type of paper.

Target Market(s)

women, young adults, expectant mothers, mothers

Industry/Entity Type

Small Business

Contact Information for Business Card

Lark Meadow Designs Essex, ON 519-608-1942 larkmeadowdesigns.ca dana@larkmeadowgiftwrapping.com find us on Friendlink

Logo Text

Lark Meadow Designs

Font styles to use
Script

Requirements
Must have
• Name, email, web address, phone number
Should not have
• cutesy graphics

```html
<!DOCTYPE html>
<html lang="en">
<head>
<meta charset="utf-8">
<title>Lark Meadow Designs – Business Card</title>
<link rel="stylesheet" href="https://fonts.googleapis.com/css2?family=Didact+Gothic&display=swap">
<style>
  :root {
    --slate-dark: #1f2427;
    --slate-mid: #3a4245;
    --lime: #74ea1f;
    --lime-deep: #5fcf12;
    --cyan: #28c8e2;
    --cyan-deep: #1aa9c4;
    --mint: #86f0c0;
    --white: #ffffff;
  }
  html, body {
    margin: 0;
    padding: 0;
    width: 1200px;
    height: 695px;
    overflow: hidden;
    background: var(--slate-dark);
  }
  .card {
    display: block;
    width: 1200px;
    height: 695px;
  }
  .card-text {
    font-family: "Didact Gothic", "Helvetica Neue", Arial, sans-serif;
  }
  .brand-name {
    fill: var(--white);
    font-size: 74px;
  }
  .brand-tagline {
    fill: var(--mint);
    font-size: 38px;
  }
  .contact-line {
    fill: var(--white);
    font-size: 30px;
    letter-spacing: 0.5px;
  }
  .band-lime { fill: url(#limeSheen); }
  .band-cyan { fill: url(#cyanSheen); }
</style>
</head>
<body>
<svg class="card" viewBox="0 0 1122 650" preserveAspectRatio="none" xmlns="http://www.w3.org/2000/svg">
  <defs>
    <radialGradient id="slateGlow" cx="0.6" cy="0.35" r="0.8">
      <stop offset="0" stop-color="var(--slate-mid)"/>
      <stop offset="1" stop-color="var(--slate-dark)"/>
    </radialGradient>
    <linearGradient id="limeSheen" x1="0" y1="0" x2="0" y2="1">
      <stop offset="0" stop-color="var(--lime)"/>
      <stop offset="1" stop-color="var(--lime-deep)"/>
    </linearGradient>
    <linearGradient id="cyanSheen" x1="0" y1="0" x2="0" y2="1">
      <stop offset="0" stop-color="var(--cyan)"/>
      <stop offset="1" stop-color="var(--cyan-deep)"/>
    </linearGradient>
  </defs>

  <rect class="card-background" width="1122" height="650" fill="url(#slateGlow)"/>

  <g class="frame-bands">
    <polygon class="band-lime" points="113,0 170,0 170,377 1122,377 1122,425 168,425 113,377"/>
    <rect class="band-cyan" x="186" y="0" width="55" height="375"/>
    <polygon class="band-cyan" points="190,428 1122,428 1122,476 245,476"/>
    <polygon class="band-lime" points="283,481 1122,481 1122,528 345,528"/>
  </g>

  <g class="corner-stripes">
    <polygon class="band-lime" points="0,405 305,650 235,650 0,462"/>
    <polygon class="band-cyan" points="0,490 200,650 135,650 0,542"/>
    <polygon class="band-lime" points="0,565 106,650 45,650 0,614"/>
  </g>

  <g class="card-text">
    <text class="brand-name" x="1020" y="148" text-anchor="end">Lark Meadow Designs</text>
    <text class="brand-tagline" x="1003" y="203" text-anchor="end">Colour &amp; Style</text>
    <text class="contact-line" x="433" y="414">tel: 519-608-1942</text>
    <text class="contact-line" x="433" y="464">web: larkmeadowdesigns.ca</text>
    <text class="contact-line" x="433" y="515">mail: dana@larkmeadowgiftwrapping.com</text>
  </g>
</svg>
</body>
</html>
```